BrambleWorks business card

Looking for business card design that supports our company/software values. We have 2 logo designs at the moment but open to change if you think you can enhance the brand. Check out website www.brambleworks.com.au.

Target Market(s)

Education

Contact Information for Business Card

Name, title, mobile, email and website

Font styles to use
Sans Serif

Colors

Designer to choose colors to be used in the design.

Requirements
Must have
• BrambleWorks logo with tree and tagline on rear side with dark grey background colour

```html
<!DOCTYPE html>
<html lang="en">
<head>
<meta charset="utf-8">
<title>BrambleWorks business card</title>
<link rel="stylesheet" href="https://fonts.googleapis.com/css2?family=Noto+Sans:wght@400;600&family=Montserrat:wght@400;500;700&display=swap">
<style>
  :root {
    --backdrop: #8d8e8e;
    --brand-blue: #05679a;
    --card-white: #ffffff;
    --ink-dark: #4a4a4a;
    --ink-text: #2f2f2f;
    --tone-warm: #e98a6a;
    --tone-violet: #8e6aa8;
    --tone-sun: #efd774;
    --feature-text: #eef5fa;
  }
  * { margin: 0; padding: 0; box-sizing: border-box; }
  html, body { width: 1200px; height: 1059px; overflow: hidden; }
  body { background: var(--backdrop); position: relative; }

  .card { position: absolute; left: 248px; width: 706px; overflow: hidden; }
  .card-front { top: 93px; height: 392px; background: var(--brand-blue); }
  .card-back { top: 526px; height: 396px; background: var(--card-white); }

  .feature {
    position: absolute;
    font-family: "Noto Sans", sans-serif;
    font-size: 17px;
    line-height: 21.7px;
    color: var(--feature-text);
  }
  .feature-left { right: 502px; text-align: right; }
  .feature-right { left: 480px; text-align: left; }

  .cycle-area {
    position: absolute; left: 239px; top: 93px;
    width: 204px; height: 204px; border-radius: 50%;
    background: radial-gradient(circle at 50% 50%, var(--brand-blue) 0 34%, transparent 35%),
                linear-gradient(135deg, var(--tone-warm), var(--tone-violet) 45%, var(--tone-sun) 75%, var(--ink-dark));
    opacity: 0.9;
  }

  .brand-lockup { position: absolute; right: 27px; top: 52px; text-align: right; }
  .brand-row { display: flex; align-items: center; gap: 10px; justify-content: flex-end; }
  .brand-dot { width: 22px; height: 22px; border-radius: 50%; background: var(--ink-dark); }
  .brand-name {
    font-family: "Noto Sans", sans-serif;
    font-size: 33px;
    font-weight: 400;
    color: var(--ink-dark);
    line-height: 38px;
  }
  .brand-tagline {
    margin-top: 6px;
    font-family: "Noto Sans", sans-serif;
    font-size: 14.5px;
    color: var(--ink-dark);
  }

  .person-name {
    position: absolute; left: 27px; top: 196px;
    font-family: "Montserrat", sans-serif; font-weight: 700;
    font-size: 25px; color: var(--brand-blue);
  }
  .person-title {
    position: absolute; left: 27px; top: 228px;
    font-family: "Montserrat", sans-serif; font-weight: 400;
    font-size: 16.5px; color: var(--ink-text);
  }
  .title-rule {
    position: absolute; left: 115px; top: 239px; width: 566px; height: 2px;
    background: var(--ink-dark);
  }
  .contact-list { position: absolute; left: 27px; top: 271px; list-style: none; }
  .contact-list li {
    display: flex; align-items: center; gap: 8px;
    height: 25px;
    font-family: "Montserrat", sans-serif; font-weight: 500;
    font-size: 17px; color: var(--ink-text);
  }
  .contact-icon { width: 16px; height: 16px; flex: none; }
  .card-wave { position: absolute; left: 0; bottom: 0; }
</style>
</head>
<body>

<section class="card card-front" aria-label="Card front: platform features">
  <div class="cycle-area" role="img" aria-label="Platform cycle diagram: discovery, insights, engage, case management"></div>

  <p class="feature feature-left" style="top:55px">Academic<br>research</p>
  <p class="feature feature-left" style="top:108px">Multi-domain<br>Assessments</p>
  <p class="feature feature-left" style="top:214px">Unlimited<br>Programs &amp;<br>Case Plans</p>
  <p class="feature feature-left" style="top:294px">Secure cloud<br>access</p>

  <p class="feature feature-right" style="top:55px">Live<br>dashboards</p>
  <p class="feature feature-right" style="top:108px">Analytics to<br>identify at-risk<br>students</p>
  <p class="feature feature-right" style="top:236px">360 degree<br>view of student</p>
  <p class="feature feature-right" style="top:292px">Team based<br>management</p>
</section>

<section class="card card-back" aria-label="Card back: contact details">
  <div class="brand-lockup">
    <div class="brand-row">
      <span class="brand-dot" aria-hidden="true"></span>
      <span class="brand-name">BrambleWorks</span>
    </div>
    <p class="brand-tagline">Student Success Platform</p>
  </div>

  <h1 class="person-name">Daniel Harcourt</h1>
  <p class="person-title">President</p>
  <div class="title-rule"></div>

  <ul class="contact-list">
    <li>
      <svg class="contact-icon" viewBox="0 0 16 16" aria-hidden="true"><path d="M3.5 1.5 L6 4.5 L4.6 6.2 C5.5 8 7.6 10.2 9.7 11.3 L11.4 9.9 L14.5 12.3 L12.9 14.5 C7.6 14.2 1.8 8.4 1.5 3.1 Z" fill="var(--brand-blue)"/></svg>
      555-318-2907
    </li>
    <li>
      <svg class="contact-icon" viewBox="0 0 16 16" aria-hidden="true"><rect x="0.5" y="3" width="15" height="10" fill="var(--brand-blue)"/><polyline points="0.8,3.5 8,9 15.2,3.5" fill="none" stroke="#fff" stroke-width="1.3"/></svg>
      info@brambleworks.com.au
    </li>
    <li>
      <svg class="contact-icon" viewBox="0 0 16 16" aria-hidden="true"><circle cx="8" cy="8" r="7.5" fill="var(--brand-blue)"/><path d="M4 4.5 C6 4 7 6 6 7.5 C5 9 6.5 10 6 12 M10 3 C11 5 12.5 5.5 13.5 6.5 M9.5 10 C10.5 9 12 10 12 12" fill="none" stroke="#fff" stroke-width="1.2"/></svg>
      www.brambleworks.com.au
    </li>
  </ul>

  <svg class="card-wave" width="706" height="52" viewBox="0 0 706 52" aria-hidden="true">
    <path d="M0 1 C140 40 300 40 440 24 C560 10 650 6 706 20 L706 31 C650 18 560 20 440 32 C300 48 140 48 0 10 Z" fill="var(--ink-dark)"/>
    <path d="M0 17 C140 54 300 52 440 37 C560 25 650 24 706 34 L706 52 L0 52 Z" fill="var(--brand-blue)"/>
  </svg>
</section>

</body>
</html>
```